Brightvale Cherries Rainier POS Card 7"H x 11"W

We are wanting to create a one-sided 7 x 11 Rainier cherry card that is eye catching and informative.This should be clear and easy to read and not cluttered. We use these cards as a display in grocery stores, demo stands, and other events to market Brightvale Rainier Cherries. We have a few facts that we would like displayed on the card (see below).

Target Market(s)

Consumers

Industry/Entity Type

Agriculture

Font styles to use
Sans Serif

Requirements
Must have
• Yellow cherries - yellow fruit (the blush on the skin is a kiss from the sun)
• Juice doesn't stain - Kid Friendly
• Add contrast to your summer table
• Sweetest Variety - still low glycemic
• Source of Vitamin C, Source of Potassium, and Source of Melatonin
• Rainiers take up to 4x as much work as red cherries
• Natural Color palettes
• Easy to read
• Brightvale Cherries
Nice to have
• Unique, creative, realistc Rainier cherry designs
Should not have
• pastel or neon color scheme, overly cutesy elements

```html
<!DOCTYPE html>
<html lang="en">
<head>
<meta charset="utf-8">
<title>Brightvale Cherries – Rainier POS Card</title>
<link rel="stylesheet" href="https://fonts.googleapis.com/css2?family=Arimo:ital,wght@0,400;0,700;1,400&family=Rubik:wght@800;900&display=swap">
<style>
  :root {
    --page: #ecebe8;
    --panel: #ffffff;
    --panel-edge: #e0708c;
    --cherry-red: #a3151b;
    --leaf-green: #2f8a3a;
    --text-grey: #5a5a5a;
    --ink: #1f1f1f;
    --sun-yellow: #f2c230;
    --sun-orange: #e8771e;
    --frame-silver: #d9dadc;
  }
  * { box-sizing: border-box; margin: 0; padding: 0; }
  html, body { width: 1200px; height: 786px; overflow: hidden; background: var(--page); }
  body { font-family: "Arimo", Arial, sans-serif; }

  .card {
    position: absolute; left: 20px; top: 24px;
    width: 1160px; height: 738px; overflow: hidden;
    box-shadow: 0 2px 10px rgba(0,0,0,.18);
  }
  .hero-photo {
    position: absolute; inset: 0;
    background:
      radial-gradient(circle at 18% 22%, #f0a03c 0 6%, transparent 16%),
      radial-gradient(circle at 62% 18%, #f2a848 0 7%, transparent 18%),
      radial-gradient(circle at 88% 10%, #e98a3a 0 6%, transparent 16%),
      radial-gradient(circle at 45% 45%, #d8472e 0 8%, transparent 20%),
      radial-gradient(circle at 75% 40%, #c93228 0 6%, transparent 18%),
      linear-gradient(135deg, #b8242a, #d9552e 45%, #b3202a);
  }
  .basket-photo {
    position: absolute; left: 600px; top: 310px;
    width: 580px; height: 470px; border-radius: 50%;
    border: 7px solid var(--frame-silver);
    box-shadow: 0 0 0 2px #8d8f93, 0 4px 14px rgba(0,0,0,.35);
    background:
      radial-gradient(ellipse at 50% 30%, #f6d25a 0 18%, transparent 40%),
      radial-gradient(ellipse at 35% 45%, #e8502c 0 10%, transparent 30%),
      radial-gradient(ellipse at 50% 85%, #8a4a22 0 25%, transparent 50%),
      linear-gradient(180deg, #c9b8a0 0%, #f0c048 35%, #e46a2e 60%, #7b4220 100%);
  }

  .info-panel {
    position: absolute; left: 0; top: 216px;
    width: 462px; height: 540px;
    background: var(--panel);
    border-top: 3px solid var(--panel-edge);
    border-right: 3px solid var(--panel-edge);
    border-top-right-radius: 70px;
    padding: 22px 0 0 34px;
  }
  .brand-kicker {
    font-family: "Rubik", sans-serif; font-weight: 800;
    font-size: 23px; line-height: 1;
    background: linear-gradient(180deg, #8fcf5a, #2f8a3a);
    -webkit-background-clip: text; background-clip: text; color: transparent;
  }
  .card-title {
    margin-top: 8px;
    font-family: "Rubik", sans-serif; font-weight: 900;
    font-size: 35px; line-height: 1; letter-spacing: .5px;
  }
  .card-title .word-green {
    background: linear-gradient(180deg, #9ccf4a, #e6c23a);
    -webkit-background-clip: text; background-clip: text; color: transparent;
  }
  .card-title .word-sun {
    background: linear-gradient(180deg, #f2c230, #e0301e);
    -webkit-background-clip: text; background-clip: text; color: transparent;
  }

  .fact-list { list-style: none; margin-top: 26px; }
  .fact {
    position: relative; padding-left: 27px;
    font-size: 14.5px; color: var(--text-grey); line-height: 1.3;
    margin-bottom: 12px;
  }
  .fact::before {
    content: ""; position: absolute; left: 0; top: 5px;
    width: 10px; height: 10px; border-radius: 50%;
    background: radial-gradient(circle at 35% 35%, #ffd27a, var(--sun-orange) 60%, #a33b14);
  }
  .fact strong { font-weight: 700; font-size: 17px; color: var(--cherry-red); }
  .fact strong.green { color: var(--leaf-green); }
  .fact strong.small { font-size: 15px; }
  .fact .note { display: block; font-size: 13.5px; }

  .tagline {
    margin-top: 14px;
    font-style: italic; font-size: 22px; line-height: 1.3; color: var(--ink);
  }
  .brand-sign {
    margin-top: 34px; display: flex; align-items: center; gap: 14px;
  }
  .brand-dot { width: 46px; height: 46px; border-radius: 50%; background: var(--cherry-red); }
  .brand-name { font-size: 34px; font-weight: 700; color: var(--ink); }
</style>
</head>
<body>
  <main class="card">
    <div class="hero-photo" role="img" aria-label="Close-up photo of fresh, wet Rainier cherries with green stems"></div>
    <div class="basket-photo" role="img" aria-label="Photo of a woven basket full of yellow and red-blushed Rainier cherries"></div>

    <section class="info-panel">
      <p class="brand-kicker">Brightvale</p>
      <h1 class="card-title"><span class="word-green">CHERRIES</span> <span class="word-sun">RAINIER</span></h1>

      <ul class="fact-list">
        <li class="fact"><strong>Yellow Cherries,</strong> <strong class="green">Yellow Fruit</strong>
          <span class="note">(the blush on the skin is a kiss from the sun)</span></li>
        <li class="fact"><strong>Juice doesn't stain</strong> - Kid Friendly</li>
        <li class="fact"><strong class="small">Add contrast</strong> to your summer table</li>
        <li class="fact"><strong>Sweetest Variety</strong> - still low glycemic</li>
        <li class="fact">Source of <strong class="small">Vitamin C</strong>, Source of <strong class="small green">Potassium</strong>,<br>and Source of <strong class="small">Melatonin</strong></li>
      </ul>

      <p class="tagline">Rainiers take up to 4x as much<br>work as red cherries</p>

      <div class="brand-sign">
        <span class="brand-dot"></span>
        <span class="brand-name">Brightvale Cherries</span>
      </div>
    </section>
  </main>
</body>
</html>
```